Brightmoor Cleaning Services

need a brochure for my cleaning company. Contact info coming soon .

Target Market(s)

Cleaning Services

Industry/Entity Type

Cleaning Service

Requirements
Must have
• I attached logo for you to use.

Corporate address -
472 Kestrel Ridge W Ste 518
Tukwila, WA 98102

Phone number - 877-514-SHINE
Nice to have
• bifold brochure. I attached some samples
Should not have
• Pictures of people. Keep it clean and professional.

```html
<!DOCTYPE html>
<html lang="en">
<head>
<meta charset="utf-8">
<title>Brightmoor Cleaning Services – Bifold Brochure</title>
<link rel="stylesheet" href="https://fonts.googleapis.com/css2?family=Poppins:wght@600;800;900&family=Roboto:wght@400;500;700&display=swap">
<style>
  :root{
    --brand-blue:#1565c0;
    --brand-blue-deep:#0d4fa3;
    --brand-red:#e31e24;
    --ink:#3a3a3a;
    --paper:#ffffff;
    --backdrop:#e4e4e4;
  }
  *{box-sizing:border-box;margin:0;padding:0}
  html,body{width:1200px;height:4000px;overflow:hidden}
  body{background:var(--backdrop);font-family:"Roboto",Arial,sans-serif;color:var(--ink);position:relative}

  .spread{position:absolute;left:60px;width:1080px;height:860px;background:var(--paper);overflow:hidden;box-shadow:0 6px 18px rgba(0,0,0,.18)}
  .spread--outer{top:120px}
  .spread--inner{top:1080px}

  .abs{position:absolute}
  .heading{font-family:"Roboto",Arial,sans-serif;font-weight:700;font-size:19px;color:var(--brand-blue);text-transform:uppercase;letter-spacing:.2px}
  .heading .accent{color:var(--brand-red)}
  .body-copy{font-size:12.5px;line-height:16px;color:var(--ink)}
  .justify{text-align:justify}

  .brand-name{font-family:"Roboto",Arial,sans-serif;font-weight:700;color:var(--brand-blue);line-height:1.05;display:flex;align-items:center;gap:10px}
  .brand-name .dot{width:14px;height:14px;border-radius:50%;background:var(--brand-red);flex:none}
  .brand-name--light{color:var(--paper)}

  .photo{position:absolute;border-radius:50%;overflow:hidden}
  .placeholder{position:absolute}

  .contact-divider{left:232px;top:690px;width:2px;height:110px;background:#cfcfcf}
  .contact-list{left:256px;top:690px;list-style:none}
  .contact-list li{display:flex;align-items:flex-start;gap:8px;font-size:12.5px;line-height:15px;margin-bottom:11px;color:var(--ink)}
  .contact-list svg{flex:none;margin-top:1px}

  .cover-title{left:560px;width:520px;text-align:center}
  .cover-title h1{font-family:"Poppins",Arial,sans-serif;font-weight:900;font-size:46px;color:var(--brand-blue);line-height:1;letter-spacing:.5px}
  .cover-title h2{font-family:"Poppins",Arial,sans-serif;font-weight:800;font-size:26px;color:var(--brand-red);line-height:1.1;margin-top:4px}
  .cover-title p{font-size:13px;line-height:16px;margin:8px auto 0;width:430px}
  .url-pill{display:inline-block;margin-top:14px;background:var(--brand-blue);color:var(--paper);font-weight:500;font-size:14px;padding:5px 26px;border-radius:20px}

  .bullets{list-style:none}
  .bullets li{position:relative;padding-left:18px;font-size:12.5px;line-height:16px;margin-bottom:10px}
  .bullets li::before{content:"";position:absolute;left:2px;top:4px;border-left:8px solid var(--brand-blue);border-top:4.5px solid transparent;border-bottom:4.5px solid transparent}
</style>
</head>
<body>

<!-- Outer spread: back page + front cover -->
<section class="spread spread--outer">
  <svg class="abs" style="left:0;top:0" width="1080" height="860" aria-hidden="true">
    <defs><clipPath id="coverClip"><rect x="540" y="0" width="540" height="860"/></clipPath></defs>
    <g clip-path="url(#coverClip)">
      <rect x="540" y="0" width="540" height="470" fill="var(--brand-blue)"/>
      <circle cx="775" cy="350" r="320" fill="var(--brand-blue)"/>
      <rect x="540" y="470" width="540" height="390" fill="var(--paper)"/>
      <circle cx="780" cy="370" r="262" fill="var(--paper)"/>
      <path d="M540 470 H1080 V560 Q 900 470 780 632 Z" fill="var(--paper)"/>
    </g>
    <circle cx="780" cy="370" r="252" fill="none" stroke="var(--brand-red)" stroke-width="7" stroke-dasharray="720 900" transform="rotate(-20 780 370)"/>
  </svg>

  <!-- back page -->
  <h3 class="heading abs" style="left:43px;top:48px">About <span class="accent">Us</span></h3>
  <p class="body-copy abs" style="left:43px;top:78px;width:310px">Lorem ipsum dolor sit amet, consectetur adipiscing elit. Curabitur cursus, neque quis faucibus convallis, libero urna ultrices diam, at fermentum odio nunc at quam. Curabitur cursus nunc massa, vitae efficitur nulla vulputate quis. Morbi porttitor enim id efficitur commodo. Nulla a magna eget nibh consectetur vehicula. Nam ullamcorper metus sit amet nulla porttitor vulputate. Suspendisse a orci tempus, auctor massa ut, accumsan neque. Mauris in libero pellentesque, semper ligula ut, maximus metus. Praesent laoreet sapien non porttitor tempus. Nunc facilisis imperdiet quam eget luctus. Nam nisi quam, tincidunt a leo at, pharetra placerat velit. Fusce tempor sollicitudin leo, quis posuere purus congue a. Vestibulum ante ipsum primis in faucibus orci luctus et ultrices posuere cubilia curae; Pellentesque varius feugiat rutrum. Nulla accumsan urna vel libero luctus, vel suscipit quam porttitor. Nullam vel enim ac nulla finibus mollis.</p>

  <h3 class="heading abs" style="left:43px;top:418px">Lorem Ipsum <span class="accent">Dolor</span></h3>
  <p class="body-copy abs" style="left:43px;top:448px;width:232px">Integer tempor mollis vestibulum. Etiam velit turpis, lobortis ac euismod et, porta in tortor. Nulla suscipit, lectus sed tincidunt elementum, justo massa malesuada justo, in iaculis nisi arcu ut magna. Morbi tristique convallis augue sit amet mattis. Pellentesque eu leo quis leo rhoncus pulvinar. Duis lacinia dolor sit amet dapibus lacinia. Donec sodales laoreet ornare.</p>
  <div class="placeholder" role="img" aria-label="Basket of cleaning supplies with sprays, brushes and gloves" style="left:285px;top:440px;width:235px;height:175px;border-radius:18px;background:linear-gradient(135deg,#e8f0fb 0%,#6fa3e0 45%,#f2c94c 75%,#e85a4f 100%)"></div>

  <div class="brand-name abs" style="left:43px;top:716px;width:170px;font-size:19px"><span class="dot"></span>Brightmoor Cleaning Services</div>
  <div class="contact-divider abs"></div>
  <ul class="contact-list abs">
    <li><svg width="13" height="13" viewBox="0 0 24 24" fill="var(--brand-red)"><path d="M6.6 10.8a15.1 15.1 0 0 0 6.6 6.6l2.2-2.2a1 1 0 0 1 1-.25 11.4 11.4 0 0 0 3.6.57 1 1 0 0 1 1 1V20a1 1 0 0 1-1 1A17 17 0 0 1 3 4a1 1 0 0 1 1-1h3.5a1 1 0 0 1 1 1c0 1.25.2 2.45.57 3.57a1 1 0 0 1-.25 1z"/></svg>877-514-SHINE</li>
    <li><svg width="13" height="13" viewBox="0 0 24 24" fill="var(--brand-red)"><path d="M2 5h20v14H2z M2 5l10 8 10-8" stroke="#fff" stroke-width="1.5"/></svg>info@brightmoorcleaning.com</li>
    <li><svg width="13" height="13" viewBox="0 0 24 24" fill="none" stroke="var(--brand-red)" stroke-width="2.5"><circle cx="12" cy="12" r="9"/><path d="M3 12h18M12 3c3 3.5 3 14.5 0 18M12 3c-3 3.5-3 14.5 0 18"/></svg>www.brightmoorcleaning.com</li>
    <li><svg width="13" height="13" viewBox="0 0 24 24" fill="var(--brand-red)"><path d="M12 2a7 7 0 0 0-7 7c0 5.2 7 13 7 13s7-7.8 7-13a7 7 0 0 0-7-7zm0 9.5A2.5 2.5 0 1 1 12 6.5a2.5 2.5 0 0 1 0 5z"/></svg>472 Kestrel Ridge W Ste 518<br>Tukwila, WA 98102</li>
  </ul>

  <!-- front cover -->
  <div class="brand-name brand-name--light abs" style="left:760px;top:40px;width:220px;font-size:22px"><span class="dot"></span>Brightmoor Cleaning Services</div>
  <div class="photo" role="img" aria-label="Bucket of colourful cleaning bottles with rubber gloves" style="left:540px;top:130px;width:480px;height:480px;background:radial-gradient(circle at 50% 35%,#fff6d8 0%,#f6d46b 35%,#4fa0e0 65%,#1f6fc4 100%)"></div>
  <div class="cover-title abs" style="top:630px">
    <h1>LOREM IPSUM</h1>
    <h2>CONSECTETUR ADIPISCING ELIT</h2>
    <p>Suspendisse a orci tempus, auctor massa ut, accumsan neque libero urna ultrices diam, at fermentum odio nunc at quam</p>
    <span class="url-pill">www.brightmoorcleaning.com</span>
  </div>
</section>

<!-- Inner spread -->
<section class="spread spread--inner">
  <svg class="abs" style="left:0;top:0" width="540" height="360" aria-hidden="true">
    <ellipse cx="270" cy="20" rx="245" ry="330" fill="var(--brand-blue)"/>
  </svg>
  <div class="placeholder" role="img" aria-label="Cleaning spray bottles, cloths and yellow rubber gloves" style="left:60px;top:55px;width:340px;height:265px;border-radius:24px;background:linear-gradient(160deg,#dfeefc 0%,#4b98e2 40%,#f5d24a 72%,#e2574c 100%)"></div>
  <div class="brand-name brand-name--light abs" style="left:300px;top:40px;width:190px;font-size:19px"><span class="dot"></span>Brightmoor Cleaning Services</div>

  <h3 class="heading abs" style="left:45px;top:336px">Ut Mollis Sapien <span class="accent">Et</span></h3>
  <p class="body-copy abs justify" style="left:45px;top:366px;width:460px">Integer tempor mollis vestibulum. Etiam velit turpis, lobortis ac euismod et, porta in tortor. Nulla suscipit, lectus sed tincidunt elementum, justo massa malesuada justo, in iaculis nisi arcu ut magna. Morbi tristique convallis augue sit amet mattis. Pellentesque eu leo quis leo rhoncus pulvinar. Duis lacinia dolor sit amet dapibus lacinia.</p>

  <h3 class="heading abs" style="left:45px;top:493px">Lorem Ipsum <span class="accent">Dolor</span></h3>
  <p class="body-copy abs justify" style="left:45px;top:523px;width:215px">Ut diam tortor, maximus sed lorem quis, vulputate scelerisque sapien. Ut mollis sapien et arcu elementum, sit amet cursus nisl semper. Suspendisse velit felis, laoreet eget laoreet vel, iaculis vel massa. Integer quis elit eleifend, pharetra sem ut, sodales orci. Duis dapibus sit amet est et rutrum. Maecenas sit amet neque vel neque blandit tempus sed sit amet ante. Pellentesque finibus egestas porta. Vivamus cursus dui magna, tempus dictum orci sodales sit amet. Vivamus vel arcu quis mi pulvinar blandit. Donec et nibh facilisis, venenatis nunc et.</p>
  <p class="body-copy abs justify" style="left:290px;top:523px;width:215px">Ut diam tortor, maximus sed lorem quis, vulputate scelerisque sapien. Ut mollis sapien et arcu elementum, sit amet cursus nisl semper. Suspendisse velit felis, laoreet eget laoreet vel, iaculis vel massa. Integer quis elit eleifend, pharetra sem ut, sodales orci. Duis dapibus sit amet est et rutrum. Maecenas sit amet neque vel neque blandit tempus sed sit amet ante. Pellentesque finibus egestas porta. Vivamus cursus dui magna, tempus dictum orci sodales sit amet. Vivamus vel arcu quis mi pulvinar blandit. Donec et nibh facilisis, venenatis nunc et.</p>

  <h3 class="heading abs" style="left:578px;top:62px">Ut Mollis Sapien <span class="accent">Et</span></h3>
  <p class="body-copy abs" style="left:578px;top:92px;width:460px">Integer tempor mollis vestibulum. Etiam velit turpis, lobortis ac euismod et, porta in tortor. Nulla suscipit, lectus sed tincidunt elementum, justo massa malesuada justo, in iaculis nisi arcu ut magna. Morbi tristique convallis augue sit amet mattis. Pellentesque eu leo quis leo rhoncus pulvinar. Duis lacinia dolor sit amet dapibus lacinia. Donec sodales laoreet ornare.</p>

  <h3 class="heading abs" style="left:578px;top:215px">Sem Egestas <span class="accent">Dolor</span></h3>
  <p class="body-copy abs justify" style="left:578px;top:245px;width:228px">Integer tempor mollis vestibulum. Etiam velit turpis, lobortis ac euismod et, porta in tortor. Nulla suscipit, lectus sed tincidunt elementum, justo massa malesuada justo, in iaculis nisi arcu ut magna. Morbi tristique convallis augue sit amet mattis. Pellentesque eu leo quis leo rhoncus pulvinar. Duis lacinia dolor sit amet dapibus lacinia. Donec sodales laoreet ornare.</p>

  <h3 class="heading abs" style="left:832px;top:215px">Ultricies <span class="accent">Risus</span></h3>
  <ul class="bullets abs" style="left:832px;top:245px;width:210px">
    <li>Lorem ipsum dolor sit amet, consectetur adipiscing elit.</li>
    <li>Curabitur cursus, neque quis faucibus convallis, libero urna ultrices diam</li>
    <li>Curabitur cursus, neque quis faucibus convallis, libero urna ultrices diam</li>
  </ul>

  <svg class="abs" style="left:0;top:0" width="1080" height="860" aria-hidden="true">
    <circle cx="860" cy="622" r="198" fill="none" stroke="var(--brand-red)" stroke-width="7" stroke-dasharray="640 800" transform="rotate(-10 860 622)"/>
  </svg>
  <div class="photo" role="img" aria-label="Vacuum cleaner on a carpet in front of a sofa" style="left:674px;top:436px;width:372px;height:372px;background:linear-gradient(170deg,#f1ece6 0%,#cfc6bc 45%,#9a9aa3 80%,#7d8089 100%)"></div>
  <div class="brand-name abs" style="left:582px;top:500px;width:190px;font-size:19px"><span class="dot"></span>Brightmoor Cleaning Services</div>
</section>

</body>
</html>
```